Need corporate powerpoint template design for our sales proposals

Need corporate power point design template for our sales proposals. This powerpoint will be targeted at our customers when we are putting design proposals and pricing quotes together for them

Target Market(s)

Our customers

Industry/Entity Type

Sales

Requirements
Must have
• Brookvane name and logo somewhere
• Would like to have a cover slide and then non-cover slide as well as an ending slide for powerpoint templates
• Must have our corporate address and contact info somewhere, they are: Brookvane, Inc PO Box 47193 Oakland, California 94620. Office # 510-384-7159, email is info@brookvane-example.com
• I also attached an example business card to give you a sense of our design, also our website is www.brookvane-example.com
• Would like to match existing color scheme

```html
<!DOCTYPE html>
<html lang="en">
<head>
<meta charset="utf-8">
<title>Brookvane Presentation Template</title>
<link href="https://fonts.googleapis.com/css2?family=Open+Sans:wght@400;600;700&display=swap" rel="stylesheet">
<style>
:root{
  --page:#c8c8c8;
  --white:#ffffff;
  --forest:#3f5e2c;
  --leaf:#5f9c3c;
  --leaf-soft:#8cc06a;
  --leaf-title:#6aa232;
  --bright:#12a64c;
  --olive:#6fae44;
  --rust:#c9782c;
  --blue:#1f6fb5;
  --ink:#6b6b6b;
}
*{margin:0;padding:0;box-sizing:border-box}
html,body{width:1059px;height:1200px;overflow:hidden;background:var(--page);font-family:"Open Sans",Arial,sans-serif}
.canvas{position:relative;width:1059px;height:1200px}
.slide{position:absolute;width:396px;height:222px;background:var(--white);overflow:hidden;box-shadow:0 3px 6px rgba(0,0,0,.28)}
.col-a{left:98px}.col-b{left:547px}
.row-1{top:100px}.row-2{top:361px}.row-3{top:622px}.row-4{top:880px}
.photo{position:absolute}
.fine{font-size:3.6px;line-height:4.6px;color:var(--ink);text-align:justify}
.slide-title{position:absolute;left:0;width:100%;text-align:center;color:var(--leaf-title);font-weight:600;font-size:13px}

/* cover */
.cover .photo{inset:0;background:radial-gradient(circle at 70% 55%,#5d7a3c 0,#44632f 40%,#34502a 100%)}
.cover .rule{position:absolute;left:106px;width:184px;height:1px;background:var(--leaf-soft)}
.cover .brand{position:absolute;top:104px;left:0;width:396px;text-align:center;color:var(--leaf-soft);font-size:19px;font-weight:400}
.cover .contact{position:absolute;top:153px;left:140px;width:150px;font-size:5.4px;line-height:6.6px;color:#d7e3cc;text-align:center}

/* about */
.about .photo-a{left:0;top:0;width:19px;height:222px;background:linear-gradient(#7aa0c8,#8c8f92)}
.about .panel{position:absolute;left:19px;top:0;width:211px;height:222px;background:var(--leaf)}
.about .photo-b{left:230px;top:0;width:166px;height:222px;background:linear-gradient(170deg,#6ea6dd 0,#9cc3e6 35%,#3f7a2e 60%,#79a94a 100%)}
.about h2{position:absolute;left:44px;top:37px;color:var(--white);font-size:14px;font-weight:700}
.about .body{position:absolute;left:44px;top:66px;width:168px}
.about .fine{color:#eef5e8;font-size:3.3px;line-height:4.55px}
.about .fine+.fine{margin-top:5px}

/* team */
.member{position:absolute;top:59px;width:80px;text-align:center}
.member .portrait{width:56px;height:56px;margin:0 auto;border-radius:50%;background:radial-gradient(circle at 50% 40%,#d4d4d4,#8a8a8a)}
.member .name{margin-top:9px;font-size:7px;font-weight:600;color:var(--leaf-title)}
.member .role{font-size:5.2px;color:var(--rust)}
.team .body{position:absolute;left:39px;top:163px;width:319px}
.team .fine{text-align:center;font-size:3.4px;line-height:4.9px}

/* facilities */
.feature{position:absolute;width:74px}
.feature svg{display:block;width:14px;height:14px}
.feature .label{margin-top:4px;font-size:6px;font-weight:600;color:#6b6b6b}
.feature .fine{font-size:3.4px;line-height:4.3px;text-align:left;margin-top:2px}

/* info split */
.split .photo{left:0;top:0;width:191px;height:222px;background:linear-gradient(135deg,#d8d84a 0,#7da84a 40%,#3d6a8c 70%,#b5793e 100%)}
.split h2{position:absolute;left:218px;width:152px;top:30px;text-align:center;color:var(--leaf-title);font-size:12px;font-weight:600}
.split .lead{position:absolute;left:218px;top:60px;width:152px}
.split .lead .fine{text-align:center;font-size:3.6px;line-height:4.9px}
.point{position:absolute;top:136px;width:72px;text-align:center}
.point svg{width:20px;height:20px}
.point .fine{text-align:center;font-size:3.6px;line-height:4.9px;margin-top:7px}

/* feature card */
.spotlight .backdrop{inset:0;background:linear-gradient(90deg,#6f9e5a,#88b071 50%,#6f9e5a)}
.spotlight .card{position:absolute;left:47px;top:37px;width:300px;height:149px;background:var(--white);overflow:hidden}
.spotlight .card-photo{left:0;top:0;width:156px;height:149px;background:linear-gradient(135deg,#3f7a34 0,#a7c98a 45%,#e8d8c6 60%,#b44a55 100%)}
.spotlight h3{position:absolute;left:166px;top:15px;width:124px;text-align:center;color:var(--blue);font-size:8px;font-weight:700}
.spotlight .body{position:absolute;left:168px;top:38px;width:122px}
.spotlight .fine{text-align:center;font-size:3.4px;line-height:4.55px}

/* timeline */
.track{position:absolute;top:46px;width:136px;height:160px}
.track .tab{position:absolute;left:0;top:0;width:135px;height:11px;border-radius:4px 4px 0 0;color:var(--white);font-size:4.8px;font-weight:700;text-align:center;line-height:11px}
.track .spine{position:absolute;left:7px;top:11px;width:1px}
.track .dot{position:absolute;left:1px;width:13px;height:13px;border-radius:50%}
.track .step{position:absolute;left:29px;width:107px;border-radius:4px;color:var(--white);font-size:6px;font-weight:400;line-height:6.8px;text-align:center;display:flex;align-items:center;justify-content:center;padding:0 6px}
.track .step::before{content:"";position:absolute;left:-6px;top:50%;margin-top:-4px;border-style:solid;border-width:4px 6px 4px 0;border-color:transparent var(--c) transparent transparent}
.track.bright{--c:var(--bright)}
.track.olive{--c:var(--olive)}
.track .tab,.track .dot,.track .step,.track .spine{background:var(--c)}

/* closing */
.closing .photo-a{left:0;top:0;width:35px;height:222px;background:linear-gradient(#6c9a3c,#c76a3e)}
.closing .band{position:absolute;top:0;height:222px;background:#9fcf7b}
.closing .panel{position:absolute;left:43px;top:0;width:150px;height:222px;background:#6fae44}
.closing .photo-b{left:201px;top:0;width:195px;height:222px;background:linear-gradient(160deg,#4f7f36 0,#d9cdb4 45%,#c9643a 80%,#b9452f 100%)}
.closing .thanks{position:absolute;left:43px;top:102px;width:150px;text-align:center;color:var(--white);font-size:13px}
.closing .thanks b{font-weight:700}
</style>
</head>
<body>
<div class="canvas">

  <section class="slide cover col-a row-1">
    <div class="photo" role="img" aria-label="Garden tools, boots and potted flowers on wooden boards under a green tint"></div>
    <div class="rule" style="top:84px"></div>
    <div class="brand">Brookvane</div>
    <div class="rule" style="top:142px"></div>
    <div class="contact">PO Box 47193 Oakland, &nbsp;510-384-7159<br>California 94620 &nbsp;info@brookvane-example.com</div>
  </section>

  <section class="slide about col-b row-1">
    <div class="photo photo-a" role="img" aria-label="Glass office building"></div>
    <div class="panel"></div>
    <div class="photo photo-b" role="img" aria-label="Office buildings beside a tree-lined path under blue sky"></div>
    <h2>About Us</h2>
    <div class="body">
      <p class="fine">Lorem ipsum dolor sit amet, consectetur adipiscing elit, sed do eiusmod tempor incididunt ut labore et dolore magna aliqua. Ut enim ad minim veniam, quis nostrud exercitation ullamco laboris nisi ut aliquip ex ea commodo consequat. Duis aute irure dolor in reprehenderit in voluptate velit esse cillum dolore eu fugiat nulla pariatur. Excepteur sint occaecat cupidatat non proident, sunt in culpa qui officia deserunt mollit anim id est laborum. Lorem ipsum dolor sit amet, consectetur adipiscing elit, sed do eiusmod tempor incididunt ut labore et dolore magna aliqua. Ut enim ad minim veniam, quis nostrud exercitation ullamco laboris nisi ut aliquip ex ea commodo consequat. Duis aute irure dolor in reprehenderit in voluptate velit esse cillum dolore eu fugiat nulla pariatur. Excepteur sint occaecat cupidatat non proident, sunt in culpa qui officia deserunt mollit anim id est laborum. Lorem ipsum dolor sit amet, consectetur adipiscing elit, sed do eiusmod tempor incididunt ut labore et dolore magna aliqua. Ut enim ad minim veniam, quis nostrud exercitation ullamco laboris nisi ut aliquip ex ea commodo consequat. Duis aute irure dolor in reprehenderit in voluptate velit esse cillum dolore eu fugiat nulla pariatur. Excepteur sint occaecat cupidatat non proident, sunt in culpa qui officia deserunt mollit anim id est laborum.</p>
      <p class="fine">Lorem ipsum dolor sit amet, consectetur adipiscing elit, sed do eiusmod tempor incididunt ut labore et dolore magna aliqua. Ut enim ad minim veniam, quis nostrud exercitation ullamco laboris nisi ut aliquip ex ea commodo consequat. Duis aute irure dolor in reprehenderit in voluptate velit esse cillum dolore eu fugiat nulla pariatur.</p>
    </div>
  </section>

  <section class="slide team col-a row-2">
    <h2 class="slide-title" style="top:21px">OUR TEAM</h2>
    <div class="member" style="left:41px"><div class="portrait" role="img" aria-label="Portrait photo of team member"></div><div class="name">CLARA WENDT</div><div class="role">General Manager</div></div>
    <div class="member" style="left:125px"><div class="portrait" role="img" aria-label="Portrait photo of team member"></div><div class="name">OWEN HALE</div><div class="role">Trainer Head</div></div>
    <div class="member" style="left:207px"><div class="portrait" role="img" aria-label="Portrait photo of team member"></div><div class="name">RAVI MENON</div><div class="role">Finance</div></div>
    <div class="member" style="left:292px"><div class="portrait" role="img" aria-label="Portrait photo of team member"></div><div class="name">THEO BRANDT</div><div class="role">Senior Trainer</div></div>
    <div class="body"><p class="fine">Lorem ipsum dolor sit amet, consectetur adipiscing elit, sed do eiusmod tempor incididunt ut labore et dolore magna aliqua. Ut enim ad minim veniam, quis nostrud exercitation ullamco laboris nisi ut aliquip ex ea commodo consequat. Duis aute irure dolor in reprehenderit in voluptate velit esse cillum dolore eu fugiat nulla pariatur. Excepteur sint occaecat cupidatat non proident, sunt in culpa qui officia deserunt mollit anim id est laborum. Lorem ipsum dolor sit amet, consectetur adipiscing elit, sed do eiusmod tempor incididunt ut labore et dolore magna aliqua. Ut enim ad minim veniam, quis nostrud exercitation ullamco laboris nisi ut aliquip ex ea commodo consequat.</p></div>
  </section>

  <section class="slide facilities col-b row-2">
    <h2 class="slide-title" style="top:21px">OUR FACILITIES</h2>
    <div class="feature" style="left:40px;top:68px">
      <svg viewBox="0 0 14 14"><rect x="1" y="4" width="12" height="8" rx="1" fill="#5f9c3c"/><rect x="5" y="2" width="4" height="3" fill="none" stroke="#5f9c3c" stroke-width="1"/><rect x="1" y="7" width="12" height="1" fill="#fff"/></svg>
      <div class="label">LOREM IPSUM</div><p class="fine">Lorem ipsum dolor sit amet, consectetur adipiscing elit, sed do eiusmod tempor incididunt ut labore</p>
    </div>
    <div class="feature" style="left:127px;top:68px">
      <svg viewBox="0 0 14 14"><rect x="1" y="2" width="12" height="11" fill="#5f9c3c"/><g fill="#fff"><rect x="3" y="6" width="2" height="2"/><rect x="6" y="6" width="2" height="2"/><rect x="9" y="6" width="2" height="2"/><rect x="3" y="9" width="2" height="2"/><rect x="6" y="9" width="2" height="2"/><rect x="9" y="9" width="2" height="2"/></g></svg>
      <div class="label">LOREM IPSUM</div><p class="fine">Lorem ipsum dolor sit amet, consectetur adipiscing elit, sed do eiusmod tempor incididunt ut labore</p>
    </div>
    <div class="feature" style="left:217px;top:68px">
      <svg viewBox="0 0 14 14"><path d="M7 1 L12 6 L10 6 L12 9 L7 11 L2 9 L4 6 L2 6 Z" fill="#5f9c3c"/><rect x="6.5" y="10" width="1" height="4" fill="#5f9c3c"/></svg>
      <div class="label">LOREM IPSUM</div><p class="fine">Lorem ipsum dolor sit amet, consectetur adipiscing elit, sed do eiusmod tempor incididunt ut labore</p>
    </div>
    <div class="feature" style="left:302px;top:68px">
      <svg viewBox="0 0 14 14"><g fill="none" stroke="#5f9c3c" stroke-width="1.4"><circle cx="7" cy="3.5" r="2.2"/><circle cx="10.5" cy="7" r="2.2"/><circle cx="7" cy="10.5" r="2.2"/><circle cx="3.5" cy="7" r="2.2"/></g><circle cx="7" cy="7" r="1.3" fill="#5f9c3c"/></svg>
      <div class="label">LOREM IPSUM</div><p class="fine">Lorem ipsum dolor sit amet, consectetur adipiscing elit, sed do eiusmod tempor incididunt ut labore</p>
    </div>
    <div class="feature" style="left:40px;top:151px">
      <svg viewBox="0 0 14 14"><path d="M3 8 a3 3 0 0 1 2-5 a3.5 3.5 0 0 1 6 1 a2.5 2.5 0 0 1 0 4 Z" fill="#5f9c3c"/><g stroke="#5f9c3c" stroke-width="1"><line x1="4" y1="10" x2="3.5" y2="13"/><line x1="7" y1="10" x2="6.5" y2="13"/><line x1="10" y1="10" x2="9.5" y2="13"/></g></svg>
      <div class="label">LOREM IPSUM</div><p class="fine">Lorem ipsum dolor sit amet, consectetur adipiscing elit, sed do eiusmod tempor incididunt ut labore</p>
    </div>
    <div class="feature" style="left:127px;top:151px">
      <svg viewBox="0 0 14 14"><rect x="2" y="1" width="10" height="9" rx="2" fill="#5f9c3c"/><rect x="4" y="3" width="6" height="4" fill="#fff"/><rect x="5" y="10" width="4" height="3" fill="#5f9c3c"/></svg>
      <div class="label">LOREM IPSUM</div><p class="fine">Lorem ipsum dolor sit amet, consectetur adipiscing elit, sed do eiusmod tempor incididunt ut labore</p>
    </div>
    <div class="feature" style="left:217px;top:151px">
      <svg viewBox="0 0 14 14"><path d="M1 2 H3 L5 9 H12 L13 4 H4" fill="none" stroke="#5f9c3c" stroke-width="1.4"/><rect x="4.5" y="4" width="8" height="5" fill="#5f9c3c"/><circle cx="6" cy="12" r="1.2" fill="#5f9c3c"/><circle cx="11" cy="12" r="1.2" fill="#5f9c3c"/></svg>
      <div class="label">LOREM IPSUM</div><p class="fine">Lorem ipsum dolor sit amet, consectetur adipiscing elit, sed do eiusmod tempor incididunt ut labore</p>
    </div>
    <div class="feature" style="left:302px;top:151px">
      <svg viewBox="0 0 14 14"><path d="M7 1 L13 7 H11 V13 H3 V7 H1 Z" fill="#5f9c3c"/><rect x="6" y="9" width="2" height="4" fill="#fff"/></svg>
      <div class="label">LOREM IPSUM</div><p class="fine">Lorem ipsum dolor sit amet, consectetur adipiscing elit, sed do eiusmod tempor incididunt ut labore</p>
    </div>
  </section>

  <section class="slide split col-a row-3">
    <div class="photo" role="img" aria-label="Gardener in apron holding a basket of potted herbs beside daisies and garden tools"></div>
    <h2>LOREM IPSUM</h2>
    <div class="lead"><p class="fine">Lorem ipsum dolor sit amet, consectetur adipiscing elit, sed do eiusmod tempor incididunt ut labore et dolore magna aliqua. Ut enim ad minim veniam, quis nostrud exercitation ullamco laboris nisi ut aliquip ex ea commodo consequat. Duis aute irure dolor in reprehenderit in voluptate velit esse cillum dolore eu fugiat nulla pariatur. Excepteur sint occaecat cupidatat non</p></div>
    <div class="point" style="left:211px">
      <svg viewBox="0 0 20 20"><path d="M4 11 a6 6 0 0 1 12 0" fill="none" stroke="#5f9c3c" stroke-width="1.8"/><rect x="2.5" y="10" width="3" height="5" rx="1" fill="#5f9c3c"/><rect x="14.5" y="10" width="3" height="5" rx="1" fill="#5f9c3c"/><path d="M5 18 Q10 14 15 18 Z" fill="#5f9c3c"/></svg>
      <p class="fine">Lorem ipsum dolor sit amet, consectetur adipiscing elit, sed do eiusmod tempor incididunt ut</p>
    </div>
    <div class="point" style="left:298px">
      <svg viewBox="0 0 20 20"><circle cx="10" cy="10" r="6.5" fill="none" stroke="#5f9c3c" stroke-width="3" stroke-dasharray="2.6 1.5"/><circle cx="10" cy="10" r="5" fill="none" stroke="#5f9c3c" stroke-width="1.6"/><circle cx="10" cy="10" r="2" fill="#5f9c3c"/></svg>
      <p class="fine">Lorem ipsum dolor sit amet, consectetur adipiscing elit, sed do eiusmod tempor incididunt ut labore et dolore</p>
    </div>
  </section>

  <section class="slide spotlight col-b row-3">
    <div class="photo backdrop" role="img" aria-label="Greenhouse interior under a green tint"></div>
    <div class="card">
      <div class="photo card-photo" role="img" aria-label="Florist tending potted flowers in a greenhouse"></div>
      <h3>LOREM IPSUM</h3>
      <div class="body"><p class="fine">Lorem ipsum dolor sit amet, consectetur adipiscing elit, sed do eiusmod tempor incididunt ut labore et dolore magna aliqua. Ut enim ad minim veniam, quis nostrud exercitation ullamco laboris nisi ut aliquip ex ea commodo consequat. Duis aute irure dolor in reprehenderit in voluptate velit esse cillum dolore eu fugiat nulla pariatur. Excepteur sint occaecat cupidatat non proident, sunt in culpa qui officia deserunt mollit anim id est laborum. Lorem ipsum dolor sit amet, consectetur adipiscing elit, sed do eiusmod tempor incididunt ut labore et dolore magna aliqua. Ut enim ad minim veniam, quis nostrud exercitation ullamco laboris nisi ut aliquip ex ea commodo consequat. Duis aute irure dolor in reprehenderit in voluptate velit esse cillum dolore eu fugiat nulla pariatur. Excepteur sint occaecat cupidatat non proident, sunt in culpa qui officia deserunt mollit anim id est laborum.</p></div>
    </div>
  </section>

  <section class="slide timeline col-a row-4">
    <h2 class="slide-title" style="top:17px">LOREM IPSUM DOLOR</h2>
    <div class="track bright" style="left:27px">
      <div class="tab">LOREM IPSUM</div>
      <div class="spine" style="height:138px"></div>
      <div class="dot" style="top:42px"></div>
      <div class="dot" style="top:90px"></div>
      <div class="dot" style="top:141px"></div>
      <div class="step" style="top:26px;height:38px">Lorem ipsum dolor sit amet, consectetur adipiscing elit, sed do dolore magna aliqua.</div>
      <div class="step" style="top:77px;height:38px">Lorem ipsum dolor sit amet, consectetur adipiscing elit, sed do dolore magna aliqua.</div>
      <div class="step" style="top:127px;height:38px">Lorem ipsum dolor sit amet, consectetur adipiscing elit, sed do dolore magna aliqua.</div>
    </div>
    <div class="track olive" style="left:212px">
      <div class="tab">LOREM IPSUM</div>
      <div class="spine" style="height:128px"></div>
      <div class="dot" style="top:38px"></div>
      <div class="dot" style="top:82px"></div>
      <div class="dot" style="top:129px"></div>
      <div class="step" style="top:26px;height:32px">Lorem ipsum dolor sit amet, consectetur adipiscing elit, sed do dolore magna aliqua.</div>
      <div class="step" style="top:71px;height:32px">Lorem ipsum dolor sit amet, consectetur adipiscing elit, sed do dolore magna aliqua.</div>
      <div class="step" style="top:116px;height:35px">Lorem ipsum dolor sit amet, consectetur adipiscing elit, sed do dolore magna aliqua.</div>
    </div>
  </section>

  <section class="slide closing col-b row-4">
    <div class="photo photo-a" role="img" aria-label="Climbing plants and terracotta pot"></div>
    <div class="band" style="left:35px;width:8px"></div>
    <div class="panel"></div>
    <div class="band" style="left:193px;width:8px"></div>
    <div class="photo photo-b" role="img" aria-label="Terracotta pots of flowers and ivy on a stone wall"></div>
    <div class="thanks">THANK <b>YOU</b></div>
  </section>

</div>
</body>
</html>
```